Need a Brochure Design

We need a brochure designed (A4 two sides or A3 foldable which is equal to 2 x A4 = total of four pages )

Brief and Logo attached.

```html
<!DOCTYPE html>
<html lang="en">
<head>
<meta charset="utf-8">
<title>RoomReady Styling Brochure</title>
<link rel="stylesheet" href="https://fonts.googleapis.com/css2?family=Rubik:wght@300;400;500&family=Yellowtail&display=swap">
<style>
:root{
  --bg:#efefef;
  --paper:#ffffff;
  --ink:#3d3d3d;
  --muted:#5a5a5a;
  --orange:#f28c0f;
  --cream:#f9efdc;
  --peach:#fbe3cc;
  --band:#b8b8b8;
  --panel:#555555;
}
*{box-sizing:border-box;margin:0;padding:0}
html,body{width:1200px;height:1200px;overflow:hidden;background:var(--bg)}
body{position:relative;font-family:"Rubik",sans-serif;color:var(--ink);font-weight:300}
.page{position:absolute;background:var(--paper);overflow:hidden}
.page::after{content:"";position:absolute;left:0;right:0;bottom:0;height:10px;background:var(--band)}
.abs{position:absolute}
.photo{position:absolute}
.script{font-family:"Yellowtail",cursive;color:var(--orange);font-weight:400}
.brand{position:absolute;display:flex;align-items:center;gap:5px;font-weight:400;color:var(--ink);white-space:nowrap}
.brand .dot{border-radius:50%;background:var(--peach);flex:none}
.head{color:var(--orange);font-weight:500}
.ticks{list-style:none}
.ticks li{position:relative;padding-left:11px}
.ticks li svg{position:absolute;left:0;top:2px;width:7px;height:7px}
.contact{display:flex;align-items:center;gap:4px;white-space:nowrap}
.contact svg{width:7px;height:7px;flex:none}

/* price sheet */
.sheet{left:199px;top:61px;width:369px;height:520px}
.sheet-title{left:0;right:0;top:18px;text-align:center;font-size:12px;font-weight:500}
.sheet-sub{left:0;right:0;top:38px;text-align:center;font-size:7.3px;line-height:9.5px;color:var(--muted)}
.pill{left:140px;top:72px;width:87px;height:14px;background:var(--orange);color:#fff;font-size:7.3px;font-weight:500;letter-spacing:1.3px;display:flex;align-items:center;justify-content:center}
.plan{font-size:7.3px;line-height:10px}
.plan b{font-weight:500;color:var(--ink)}
.plan span{color:var(--muted)}
.price{margin-top:4px;display:inline-block;border:1px solid var(--ink);border-right:none;color:var(--orange);font-weight:500;padding:1px 8px 1px 3px;font-size:7.3px;clip-path:polygon(0 0,100% 0,88% 100%,0 100%)}
.sheet .ticks{font-size:7.5px;line-height:11px;color:var(--muted);width:160px}

/* cover */
.cover{left:634px;top:61px;width:367px;height:520px}
.cover-tag{left:0;right:0;top:430px;text-align:center;font-size:17px;color:var(--ink)}
.cover-script{left:0;right:0;top:456px;text-align:center;font-size:27px}

/* spread */
.spread{left:232px;top:625px;width:736px;height:521px}
.fold{left:368px;top:0;width:1px;bottom:10px;background:#e3e3e3}
.cream{left:27px;top:0;width:153px;height:521px;background:var(--cream)}
.hey{left:56px;top:30px;font-size:27px}
.intro{left:43px;width:124px;font-size:8.6px;line-height:11.8px;color:var(--muted)}
.body-s{font-size:7.2px;line-height:10.5px;color:var(--muted)}
.body-s b{font-weight:500;color:var(--ink)}
.reward{left:535px;top:133px;width:176px;height:112px;background:var(--panel);color:#fff;text-align:center}
</style>
</head>
<body>

<!-- Price & plan sheet -->
<section class="page sheet">
  <h1 class="abs sheet-title">RoomReady Styling</h1>
  <p class="abs sheet-sub">We average over 185 property styling projects per year,<br>with a large proportion selling in less than 30 days!</p>
  <div class="abs pill">PRICE &amp; PLAN</div>

  <div class="abs plan" style="left:64px;top:94px"><b>1 Bedroom Property</b><br><span>Full Styling + 6 Weeks Free Hire*</span><br><span class="price">$2750.00 AUD</span></div>
  <div class="abs plan" style="left:197px;top:94px"><b>3 Bedroom Property</b><br><span>Full Styling + 6 Weeks Free Hire*</span><br><span class="price">$4470.00 AUD</span></div>
  <div class="abs plan" style="left:64px;top:140px"><b>2 Bedroom Property</b><br><span>Full Styling + 6 Weeks Free Hire*</span><br><span class="price">$3250.00 AUD</span></div>
  <div class="abs plan" style="left:197px;top:140px"><b>4 Bedroom Property</b><br><span>Full Styling + 6 Weeks Free Hire*</span><br><span class="price">$3897.00 AUD</span></div>

  <div class="photo" role="img" aria-label="Photo of a bright staged open-plan living, kitchen and dining area" style="left:29px;top:191px;width:310px;height:154px;background:linear-gradient(180deg,#e9e9e7,#d3d1cc 60%,#c9c4bb)"></div>

  <ul class="abs ticks" style="left:32px;top:356px">
    <li><svg viewBox="0 0 10 10"><circle cx="5" cy="5" r="4.3" fill="none" stroke="#f28c0f"/><path d="M3 5.2l1.5 1.5L7.2 3.6" fill="none" stroke="#f28c0f"/></svg>Helping your property reach its highest potential without busting the budget.</li>
    <li><svg viewBox="0 0 10 10"><circle cx="5" cy="5" r="4.3" fill="none" stroke="#f28c0f"/><path d="M3 5.2l1.5 1.5L7.2 3.6" fill="none" stroke="#f28c0f"/></svg>Achieving a record number of viewings and the highest possible sale price.</li>
    <li><svg viewBox="0 0 10 10"><circle cx="5" cy="5" r="4.3" fill="none" stroke="#f28c0f"/><path d="M3 5.2l1.5 1.5L7.2 3.6" fill="none" stroke="#f28c0f"/></svg>Installation, interior design and decoration, and removal included.</li>
  </ul>
  <ul class="abs ticks" style="left:205px;top:355px;width:140px">
    <li><svg viewBox="0 0 10 10"><circle cx="5" cy="5" r="4.3" fill="none" stroke="#f28c0f"/><path d="M3 5.2l1.5 1.5L7.2 3.6" fill="none" stroke="#f28c0f"/></svg>Pre-sale home preparation to post-sale removal.</li>
    <li><svg viewBox="0 0 10 10"><circle cx="5" cy="5" r="4.3" fill="none" stroke="#f28c0f"/><path d="M3 5.2l1.5 1.5L7.2 3.6" fill="none" stroke="#f28c0f"/></svg>Free consultation and longer rental periods.</li>
    <li><svg viewBox="0 0 10 10"><circle cx="5" cy="5" r="4.3" fill="none" stroke="#f28c0f"/><path d="M3 5.2l1.5 1.5L7.2 3.6" fill="none" stroke="#f28c0f"/></svg>A small investment for such a large transformation!</li>
  </ul>

  <div class="brand" style="left:66px;top:462px;font-size:8px"><span class="dot" style="width:14px;height:14px"></span>RoomReady Styling</div>
  <div class="abs" style="left:171px;top:453px;font-size:7.3px;line-height:11.7px;color:var(--muted)">
    <div class="contact"><svg viewBox="0 0 10 10"><path d="M2.5 1.5l1.5 2-1 1c.6 1.3 1.3 2 2.5 2.5l1-1 2 1.5-1 1.5C4.5 9 1 5.5 1 2.5z" fill="none" stroke="#555" stroke-width=".8"/></svg>0400 123 456</div>
    <div class="contact"><svg viewBox="0 0 10 10"><circle cx="5" cy="5" r="4.2" fill="none" stroke="#555" stroke-width=".8"/><circle cx="5" cy="5" r="1.6" fill="none" stroke="#555" stroke-width=".8"/></svg>hello@roomreadystyling.com.au</div>
    <div class="contact"><svg viewBox="0 0 10 10"><circle cx="5" cy="5" r="4.2" fill="none" stroke="#555" stroke-width=".8"/><path d="M1 5h8M5 1c-2 2.5-2 5.5 0 8M5 1c2 2.5 2 5.5 0 8" fill="none" stroke="#555" stroke-width=".6"/></svg>roomreadystyling.com.au</div>
  </div>
</section>

<!-- Cover -->
<section class="page cover">
  <div class="brand" style="left:108px;top:80px;font-size:13px"><span class="dot" style="width:22px;height:22px"></span>RoomReady Styling</div>
  <div class="photo" role="img" aria-label="Photo of a staged living room with grey sofas, coffee table and wall art" style="left:28px;top:167px;width:310px;height:153px;background:linear-gradient(180deg,#ececea,#d9d7d2 55%,#c4bcae)"></div>
  <div class="photo" role="img" aria-label="Photo of cushions and plant on a sofa" style="left:28px;top:324px;width:61px;height:78px;background:linear-gradient(180deg,#d8d2c6,#6f7a78)"></div>
  <div class="photo" role="img" aria-label="Photo of a styled hallway and study desk" style="left:93px;top:324px;width:183px;height:78px;background:linear-gradient(90deg,#e6e6e6,#dcd9d4 60%,#cfc6bb)"></div>
  <div class="photo" role="img" aria-label="Photo of a styled bedroom with artwork" style="left:281px;top:324px;width:58px;height:78px;background:linear-gradient(180deg,#b9b39f,#e8e6e0)"></div>
  <p class="abs cover-tag">We Will Give Your Property</p>
  <p class="abs script cover-script">The Best Look!</p>
</section>

<!-- Inner spread -->
<section class="page spread">
  <div class="abs cream"></div>
  <div class="abs fold"></div>
  <p class="abs script hey">Hey there,</p>
  <p class="abs intro" style="top:80px">I'm Mira, Owner and Creative Director of RoomReady Styling. Please let me introduce you to our amazingly creative property styling team!</p>
  <p class="abs intro" style="top:146px">We are a friendly bunch who are passionate about home staging. We've been property staging apartments, townhouses, and standalone homes since 2009. An all-female powerhouse, we combine our experience in art, interior design, retail, and business to offer professional home styling throughout Melbourne.</p>
  <div class="photo" role="img" aria-label="Portrait of the company owner" style="left:11px;top:301px;width:174px;height:211px;background:linear-gradient(180deg,var(--cream),#e9e3da 55%,#3a3a3a)"></div>

  <div class="photo" role="img" aria-label="Photos of stylists arranging cushions and bedding" style="left:206px;top:42px;width:302px;height:203px;background:linear-gradient(90deg,#dcdcdc,#c9c7c4 45%,#e4e4e6 60%,#e8c9c2)"></div>
  <div class="brand" style="left:238px;top:22px;font-size:8px;background:rgba(255,255,255,.85);padding:2px 4px"><span class="dot" style="width:13px;height:13px"></span>RoomReady Styling</div>

  <h2 class="abs head" style="left:206px;top:283px;font-size:10px;line-height:12px">Because First<br>Impressions Count</h2>
  <div class="abs body-s" style="left:206px;top:316px;width:128px">
    <p>A gorgeous looking home sells faster and fetches a higher price.</p>
    <p style="margin-top:5px">At <b>RoomReady Styling</b>, we help our property clients create a lasting impression with minimal spend. Our property vendors are usually looking for home-staging on a tight budget. They come to us searching for creative transformations to help them sell well. Thoughtfully positioned furniture and on-trend interior décor can make all the difference!</p>
    <p style="margin-top:5px">Our property styling service includes a free consultation, longer rental periods, and installation and removal.</p>
  </div>

  <h2 class="abs head" style="left:535px;top:47px;font-size:10px">We're Well-connected</h2>
  <p class="abs body-s" style="left:535px;top:65px;width:178px">We have a steady flow of clients who have not yet secured their Real Estate Agents, so we'd be happy to share the love. We believe in last relationships, and we work with reputable agents across Melbourne.</p>

  <div class="abs reward">
    <p style="margin-top:10px;font-size:12px;font-weight:400">We Reward</p>
    <p class="script" style="font-size:29px;line-height:30px">Referrals!</p>
    <p style="margin-top:4px;font-size:7.3px">We offer a</p>
    <p style="font-size:12px;font-weight:500;line-height:15px">$200 GIFT VOUCHER</p>
    <p style="font-size:7.3px">for every successful referral to us!</p>
  </div>

  <h2 class="abs head" style="left:394px;top:294px;font-size:10px;line-height:12px">Why choose<br>RoomReady Styling?</h2>
  <ul class="abs ticks body-s" style="left:394px;top:325px;width:120px;line-height:10.5px">
    <li style="margin-bottom:5px"><svg viewBox="0 0 10 10"><circle cx="5" cy="5" r="4.3" fill="none" stroke="#f28c0f"/><path d="M3 5.2l1.5 1.5L7.2 3.6" fill="none" stroke="#f28c0f"/></svg>Experienced, enthusiastic property stylists</li>
    <li style="margin-bottom:5px"><svg viewBox="0 0 10 10"><circle cx="5" cy="5" r="4.3" fill="none" stroke="#f28c0f"/><path d="M3 5.2l1.5 1.5L7.2 3.6" fill="none" stroke="#f28c0f"/></svg>Work with low client budgets</li>
    <li style="margin-bottom:5px"><svg viewBox="0 0 10 10"><circle cx="5" cy="5" r="4.3" fill="none" stroke="#f28c0f"/><path d="M3 5.2l1.5 1.5L7.2 3.6" fill="none" stroke="#f28c0f"/></svg>Fast turnaround to a tight deadline</li>
    <li style="margin-bottom:5px"><svg viewBox="0 0 10 10"><circle cx="5" cy="5" r="4.3" fill="none" stroke="#f28c0f"/><path d="M3 5.2l1.5 1.5L7.2 3.6" fill="none" stroke="#f28c0f"/></svg>Flexible rental terms (4/6/8 weeks)</li>
    <li><svg viewBox="0 0 10 10"><circle cx="5" cy="5" r="4.3" fill="none" stroke="#f28c0f"/><path d="M3 5.2l1.5 1.5L7.2 3.6" fill="none" stroke="#f28c0f"/></svg>Happy to recommend potential customers</li>
  </ul>

  <div class="photo" role="img" aria-label="Group photo of the styling team" style="left:540px;top:264px;width:196px;height:196px;background:linear-gradient(180deg,#d8d8d8,#e6e6e6 45%,#b9986f 85%,#8a6a4c)"></div>

  <p class="abs" style="left:368px;right:0;top:480px;text-align:center;font-size:7.3px;color:var(--orange)">We'd love to hear from you, so please contact us by telephone, text, or email:</p>
  <div class="abs" style="left:368px;right:0;top:494px;display:flex;justify-content:center;gap:7px;font-size:7.3px;color:var(--muted)">
    <div class="contact"><svg viewBox="0 0 10 10"><path d="M2.5 1.5l1.5 2-1 1c.6 1.3 1.3 2 2.5 2.5l1-1 2 1.5-1 1.5C4.5 9 1 5.5 1 2.5z" fill="none" stroke="#555" stroke-width=".8"/></svg>0400 123 456</div>
    <div class="contact"><svg viewBox="0 0 10 10"><circle cx="5" cy="5" r="4.2" fill="none" stroke="#555" stroke-width=".8"/><circle cx="5" cy="5" r="1.6" fill="none" stroke="#555" stroke-width=".8"/></svg>hello@roomreadystyling.com.au</div>
    <div class="contact"><svg viewBox="0 0 10 10"><circle cx="5" cy="5" r="4.2" fill="none" stroke="#555" stroke-width=".8"/><path d="M1 5h8M5 1c-2 2.5-2 5.5 0 8M5 1c2 2.5 2 5.5 0 8" fill="none" stroke="#555" stroke-width=".6"/></svg>roomreadystyling.com.au</div>
  </div>
</section>

</body>
</html>
```